Custom Wordpress Theme - Original and Professional

We are a boutique IT consulting firm that provide small and medium business in Australia three different levels of IT service.
We are looking for a developer who will create a customised, original and professional wordpress theme. We are looking for the developer to create a professional, clean, clear and simple theme with a stylish layout, images and icons.
Our three services are: IT support | IT Services | IT Solutions and we would like to clearly differentiate the difference in each level of service in as few words as possible.
IT Support is the ad hock “call us, when you need us” service, that smaller business or those with minimal issues use.
IT service is the unlimited service, that business with existing (and well maintained) IT systems choose and is both flexible and scalable including no contracts or paperwork required.
IT solutions are the unlimited service that businesses that need new or updated infrastructure choose and it includes all the hardware, software and services with no contracts or any ongoing commitment.
The main page on the web site will attract the visitor to choose the right “service level” for their business and then we will have a dedicated page for each service and another page for a comparison (table) to compare all three services.
Lastly we will need a contact us page that has both office locations (Sydney and Melbourne), contact phone numbers and an email form.
Items we are focused on for this project are: 1. Images, 2.Icons 3. Layout.
In summary we are looking for a custom WordPress theme into a 6 page (Home, IT Support, IT Services, IT Solutions, Compare Service levels and Contact us) website. The design must include relevant images and icons and be clear, simple, professional and sleek.

Thank you for your time and creativity and I look forward to working with you!

Target Market(s)

Small and Medium businesses in Australia

Industry/Entity Type

Boutique

Requirements
Must have
• - 6 Pages layout: Home, IT support, IT services, IT Solutions, Compare service levels and Contact us
- Images, Layout and Icons.
- Clean, Clear, Simple, Elegant, Stylish.
Nice to have
• - Some text (if possible but not required).
Should not have
• - Complexity.
- Confusing layout.
- Generic non matching images and icons.

```html
<!DOCTYPE html>
<html lang="en">
<head>
<meta charset="utf-8">
<title>Company Name — IT Support, Services and Solutions</title>
<link href="https://fonts.googleapis.com/css2?family=Marcellus&family=Open+Sans:wght@400;600&display=swap" rel="stylesheet">
<style>
  :root {
    --accent: #3ddde3;
    --ink: #1c1c1c;
    --body: #333;
    --muted: #8a8a8a;
    --panel: #262626;
    --rule: #dcdcdc;
    --button: #ececec;
    --paper: #ffffff;
  }
  * { margin: 0; padding: 0; box-sizing: border-box; }
  html, body { width: 840px; height: 1200px; overflow: hidden; background: var(--paper); }
  body { position: relative; font-family: "Open Sans", sans-serif; color: var(--body); }
  .abs { position: absolute; }

  .brand-name { left: 45px; top: 55px; font-family: "Marcellus", serif; font-size: 22px; color: var(--ink); letter-spacing: .3px; }
  .brand-slogan { left: 65px; top: 84px; font-size: 7.5px; color: var(--muted); letter-spacing: .3px; }
  .main-nav { left: 343px; top: 63px; display: flex; gap: 16px; font-size: 12px; color: var(--ink); }
  .main-nav .current { color: var(--accent); }

  .hero-image { left: 41px; top: 119px; width: 765px; height: 293px;
    background: linear-gradient(100deg, #e9d2c6 0%, #dcc0b2 30%, #eeeeef 55%, #f5f5f6 100%); }
  .hero-card { left: 556px; top: 203px; width: 224px; height: 112px; background: var(--panel); box-shadow: 0 2px 4px rgba(0,0,0,.3); }
  .hero-card .dot { position: absolute; left: 15px; top: 24px; width: 37px; height: 37px; border-radius: 50%; background: var(--accent); }
  .hero-card h2 { position: absolute; left: 66px; top: 20px; font-family: "Marcellus", serif; font-weight: 400; font-size: 22px; color: #fff; }
  .hero-card p { position: absolute; left: 96px; top: 49px; font-size: 8px; color: #fff; letter-spacing: .2px; }

  .service { width: 230px; }
  .service .icon { position: absolute; left: 0; top: 0; }
  .service h3 { position: absolute; left: 42px; top: 0; font-family: "Marcellus", serif; font-weight: 400; font-size: 21px; color: var(--ink); white-space: nowrap; }
  .service .lead { position: absolute; left: 0; top: 39px; font-size: 9px; color: var(--accent); white-space: nowrap; }
  .service .text { position: absolute; left: 0; top: 53px; width: 230px; font-size: 7.2px; line-height: 15px; }
  .more-btn { position: absolute; left: 0; top: 150px; width: 39px; height: 28px; border-radius: 5px;
    background: linear-gradient(#f8f8f8, var(--button)); box-shadow: 0 1px 2px rgba(0,0,0,.25);
    font-size: 7.5px; color: #333; display: flex; align-items: center; justify-content: center; }

  .divider { left: 67px; top: 682px; width: 708px; border-top: 1px dashed var(--rule); }

  .feature { width: 230px; }
  .feature h4 { position: absolute; top: 0; font-family: "Open Sans", sans-serif; font-weight: 600; font-size: 11px; color: var(--ink); white-space: nowrap; }
  .feature .text { position: absolute; left: 32px; top: 21px; width: 155px; font-size: 7.2px; line-height: 11.8px; text-align: justify; }
  .feature .link { position: absolute; left: 39px; top: 107px; font-size: 7.5px; color: var(--ink); letter-spacing: .3px; }

  .consult { left: 529px; top: 717px; width: 240px; }
  .consult h4 { font-family: "Marcellus", serif; font-weight: 400; font-size: 12px; color: var(--ink); white-space: nowrap; }
  .consult .bar { margin-top: 8px; width: 208px; border-top: 2px solid var(--accent); }
  .consult .text { margin-top: 23px; width: 200px; font-size: 7.2px; line-height: 11.8px; }
  .contact-row { position: absolute; left: 0; display: flex; align-items: center; gap: 7px; font-size: 7.5px; color: var(--ink); white-space: nowrap; }
  .contact-row .tile { width: 18px; height: 24px; background: #cfcfcf; }
  .contact-row a { color: var(--accent); text-decoration: none; }
  .contact-sep { position: absolute; left: 0; width: 206px; border-top: 1px dashed var(--rule); }

  .site-footer { left: 0; top: 1154px; width: 840px; height: 46px; background: var(--accent); }
  .social { position: absolute; right: 40px; top: 18px; display: flex; gap: 4px; }
  .social span { width: 7px; height: 7px; border-radius: 50%; background: #fff; }
</style>
</head>
<body>
  <header>
    <div class="abs brand-name">COMPANY NAME</div>
    <div class="abs brand-slogan">YOUR COMPANY SOLGAN</div>
    <nav class="abs main-nav">
      <span class="current">Home</span><span>IT support</span><span>IT Services</span><span>IT Solutions</span><span>Compare Service</span><span>Contact us</span>
    </nav>
  </header>

  <div class="abs hero-image" role="img" aria-label="Photo of a hand typing on a white keyboard"></div>
  <div class="abs hero-card">
    <div class="dot"></div>
    <h2>IT SOLUTION</h2>
    <p>THINK TO AHEAD</p>
  </div>

  <section class="abs service" style="left:67px;top:437px;">
    <svg class="icon" width="24" height="24" viewBox="0 0 24 24"><rect x="3" y="5" width="18" height="13" fill="none" stroke="#3ddde3" stroke-width="2"/><rect x="1" y="19" width="22" height="3" fill="#3ddde3"/></svg>
    <h3>IT SOLUTIONS</h3>
    <p class="lead">Duirpis nteerutrm ante eu lastibulumiam</p>
    <p class="text">Estiblum ante ipsum primis faorci lucs et utrices posuere cubilipende sollicitudin veied leo pharetra aug neaugue. Nlit magnandrerit siet tinidunt aciverra sed nulla.onec porta diam eu massa. Quisque diam lorem interdum apibus ac scelerisque vitpede. Donec eget tellu.</p>
    <div class="more-btn">MORE</div>
  </section>

  <section class="abs service" style="left:310px;top:437px;">
    <svg class="icon" width="26" height="26" viewBox="0 0 26 26" style="top:4px"><circle cx="8" cy="17" r="5" fill="none" stroke="#3ddde3" stroke-width="3" stroke-dasharray="2.5 1.5"/><circle cx="18" cy="7" r="4" fill="none" stroke="#3ddde3" stroke-width="3" stroke-dasharray="2 1.5"/></svg>
    <h3 style="left:58px">IT SERVICES</h3>
    <p class="lead">Lorem ipsum dolor sit amet consectetuer</p>
    <p class="text">Cubilipende sollicitudin veied leo pharetra aug neaugue. Nlit magnandrerit siet tinidunt aciverra sed nullporta diam eu massa. Quisque diam lorem interdum apibus ac sceleripeonec eget tellu non erat lacinia feentum. Donec in velit ve</p>
    <div class="more-btn">MORE</div>
  </section>

  <section class="abs service" style="left:550px;top:437px;">
    <svg class="icon" width="20" height="24" viewBox="0 0 20 24"><circle cx="8" cy="6" r="4.5" fill="#3ddde3"/><path d="M1 23 Q1 12 8 12 Q15 12 15 23 Z" fill="#3ddde3"/></svg>
    <h3 style="left:44px">IT SUPPORT</h3>
    <p class="lead" style="left:3px">Sed ut perspiciatis unde omnis</p>
    <p class="text">Estiblum ante ipsum primis faorci lucs et utrices posuere cubilipende sollicitudin veied leo pharetra aug neaugue. Nlit magnandrerit siet tinidunt aciverra sed nulla.onec porta diam eu massa. Quisque diam lorem interdum apibus ac scelerisque vitpede. Donec eget tellu.</p>
    <div class="more-btn">MORE</div>
  </section>

  <div class="abs divider"></div>

  <section class="abs feature" style="left:118px;top:716px;">
    <svg width="20" height="20" viewBox="0 0 20 20" style="position:absolute;left:0;top:0"><rect x="7" y="1" width="11" height="15" fill="none" stroke="#3ddde3" stroke-width="1.8"/><rect x="1" y="7" width="8" height="12" fill="#fff" stroke="#3ddde3" stroke-width="1.8"/></svg>
    <h4 style="left:32px">Lorem Ipsum</h4>
    <p class="text">Estiblum ante ipsum primis faorci lucs et utrices posuere cubilipende sollicitudin veied leo pharetra aug neaugue. Nlit magnandrerit siet tinidunt aciverra sed nulla.onec porta diam eu massa. Quisque diam lorem interdum apibus ac scelerisque vitpede. Donec eget tellu.</p>
    <span class="link">MORE INFO</span>
  </section>

  <section class="abs feature" style="left:325px;top:716px;">
    <svg width="22" height="16" viewBox="0 0 22 16" style="position:absolute;left:0;top:2px"><rect x="1" y="1" width="6" height="14" fill="none" stroke="#3ddde3" stroke-width="1.8"/><rect x="15" y="1" width="6" height="14" fill="none" stroke="#3ddde3" stroke-width="1.8"/><rect x="8" y="4" width="6" height="8" fill="#3ddde3"/></svg>
    <h4 style="left:35px">Lorem Ipsum</h4>
    <p class="text" style="left:32px">Estiblum ante ipsum primis faorci lucs et utrices posuere cubilipende sollicitudin veied leo pharetra aug neaugue. Nlit magnandrerit siet tinidunt aciverra sed nulla.onec porta diam eu massa. Quisque diam lorem interdum apibus ac scelerisque vitpede. Donec eget tellu.</p>
    <span class="link" style="left:40px;top:105px">MORE INFO</span>
  </section>

  <section class="abs feature" style="left:118px;top:857px;">
    <svg width="14" height="14" viewBox="0 0 14 14" style="position:absolute;left:9px;top:2px"><circle cx="7" cy="7" r="6.5" fill="#3ddde3"/><circle cx="7" cy="7" r="2.5" fill="#fff"/></svg>
    <h4 style="left:28px">Lorem Ipsum</h4>
    <p class="text" style="top:27px">Estiblum ante ipsum primis faorci lucs et utrices posuere cubilipende sollicitudin veied leo pharetra aug neaugue. Nlit magnandrerit siet tinidunt aciverra sed nulla.onec porta diam eu massa. Quisque diam lorem interdum apibus ac scelerisque vitpede. Donec eget tellu.</p>
    <span class="link" style="left:37px;top:113px">MORE INFO</span>
  </section>

  <section class="abs feature" style="left:325px;top:857px;">
    <svg width="14" height="14" viewBox="0 0 14 14" style="position:absolute;left:8px;top:3px"><circle cx="7" cy="7" r="6" fill="none" stroke="#3ddde3" stroke-width="1.6"/><path d="M1 7 H13 M7 1 V13" stroke="#3ddde3" stroke-width="1.2"/></svg>
    <h4 style="left:37px">Lorem Ipsum</h4>
    <p class="text" style="left:32px;top:27px">Estiblum ante ipsum primis faorci lucs et utrices posuere cubilipende sollicitudin veied leo pharetra aug neaugue. Nlit magnandrerit siet tinidunt aciverra sed nulla.onec porta diam eu massa. Quisque diam lorem interdum apibus ac scelerisque vitpede. Donec eget tellu.</p>
    <span class="link" style="left:40px;top:111px">MORE INFO</span>
  </section>

  <aside class="abs consult">
    <h4>CONSULT YOUR NEEDS WITH OUR EXPERTS</h4>
    <div class="bar"></div>
    <p class="text">Estiblum ante ipsum primis faorci lucs et utrices posuere cubilipende sollicitudin veied leo</p>
    <div class="contact-sep" style="top:99px"></div>
    <div class="contact-row" style="top:109px"><span class="tile"></span>BY PHONE : 840 55 210 3397</div>
    <div class="contact-sep" style="top:140px"></div>
    <div class="contact-row" style="top:151px"><span class="tile"></span>BY EMAIL : <a>hello@northbyteit.com</a></div>
    <div class="contact-sep" style="top:188px"></div>
    <div class="contact-row" style="top:194px"><span class="tile"></span>OR <a>FILL IN THE FORM</a> ON OUR CONTACT PAGE</div>
  </aside>

  <footer class="abs site-footer">
    <div class="social"><span></span><span></span><span></span><span></span></div>
  </footer>
</body>
</html>
```